New website for Pollard Law Firm at www.keepwinning-example.com

We are a professional law firm located in the Nashville, Tennessee USA area. We focus on personal injury law. We are looking for a slick new website that is user friendly for updating with new blogs, videos, etc. The primary colors should be red, black, and white. It should load extremely fast and have a good mobile component. The pages for the design will include a home page, about us, news, contact us, and practice page. The practice page will be copied for all the practice areas including motor vehicle accidents, slip and fall accidents, dog bites, etc. We have included an image which we would like to include in the new site which shows the color scheme The image is called banner-Car Wreck. The new website should NOT have gavels, court houses, law books, scales or the typical images for a law firm.

Target Market(s)

People in Tennessee involved in accidents

Industry/Entity Type

Legal services, law firm

Coding

Coded - Design and coding required

Number of Pages Required

5+ page

Font styles to use
Serif

Colors
EB3D1F
EC4F4E
F09395
F8D3D4
FCEDEE

Requirements
Should not have
• Gavels, columns, scales, law related images

```html
<!DOCTYPE html>
<html lang="en">
<head>
<meta charset="utf-8">
<title>Pollard Law Firm</title>
<link href="https://fonts.googleapis.com/css2?family=Prata&family=Montserrat:wght@400;500;600&family=Cormorant+Garamond:wght@500&display=swap" rel="stylesheet">
<style>
:root{
  --red:#d33a3a;
  --red-dark:#b82a2a;
  --black:#111;
  --ink:#222;
  --grey-text:#555;
  --light:#ececec;
  --white:#fff;
  --line:#ddd;
}
*{box-sizing:border-box;margin:0;padding:0}
html,body{width:1200px;height:4468px;overflow:hidden}
body{position:relative;background:var(--white);font-family:"Montserrat",sans-serif;color:var(--ink)}
.abs{position:absolute}
.serif{font-family:"Prata",serif}
.eyebrow{font-size:13px;color:var(--red);letter-spacing:.5px;display:flex;align-items:center;gap:10px;text-transform:uppercase}
.eyebrow::before,.eyebrow::after{content:"";width:40px;height:1px;background:#333}
.eyebrow.center{justify-content:center}
.heading{font-family:"Prata",serif;font-size:38px;text-transform:uppercase;color:var(--black)}
.btn{display:flex;align-items:stretch;height:34px;border:1px solid var(--red);background:var(--white);font-family:"Prata",serif;font-size:13px;color:var(--black);text-transform:uppercase}
.btn .arrow{width:36px;background:var(--red);display:flex;align-items:center;justify-content:center}
.btn .label{padding:0 20px;display:flex;align-items:center}
.photo{background:linear-gradient(135deg,#8a8f96,#d6d8da)}

/* top bar */
.topbar{left:0;top:0;width:1200px;height:35px;background:var(--black);color:#ddd;font-size:12px}
.topbar span{position:absolute;top:10px;display:flex;align-items:center;gap:8px}
.nav{left:0;top:35px;width:1200px;height:55px;background:var(--white)}
.logo{font-family:"Prata",serif;color:var(--red);font-size:22px;position:absolute;left:60px;top:14px}
.menu{position:absolute;left:456px;top:18px;display:flex;gap:32px;font-size:12px;color:#444}
.menu .active{color:var(--red)}
.call{position:absolute;left:967px;top:8px;width:174px;height:37px;border:1px solid var(--red);display:flex;font-size:14px;font-weight:600}
.call .ic{width:40px;background:var(--red);display:flex;align-items:center;justify-content:center}
.call .num{display:flex;align-items:center;padding-left:12px}

/* hero */
.hero{left:0;top:90px;width:1200px;height:700px}
.hero h1{position:absolute;left:62px;top:200px;font-family:"Prata",serif;color:var(--white);font-size:68px;line-height:84px;font-weight:400}
.hero .btn{position:absolute;left:60px;top:395px}

/* about */
.about-text{left:62px;top:928px;width:425px;font-size:11.5px;line-height:20px;color:var(--grey-text)}
.about-text p{margin-bottom:14px}

/* quote */
.quote{left:537px;top:1376px;width:540px;font-family:"Cormorant Garamond",serif;font-size:30px;line-height:34px;color:var(--white)}

/* practice */
.practice-item{font-family:"Prata",serif;font-size:18px;line-height:26px;color:var(--black)}
.practice-item a{display:block;font-family:"Montserrat",sans-serif;font-size:13px;color:var(--red);text-decoration:underline;margin-top:2px}

/* news */
.news-card{left:593px;top:2712px;width:309px;height:225px;background:var(--black);color:var(--white);padding:30px 24px 0 24px;text-align:right}
.news-card h3{font-family:"Prata",serif;font-size:16px;line-height:24px;font-weight:400}
.news-card p{font-size:11px;line-height:19px;color:#ccc;margin-top:12px}
.news-card a{display:block;color:var(--red);font-size:9px;text-decoration:underline;margin-top:12px}

/* subscribe */
.subscribe{left:0;top:3052px;width:1200px;height:113px;background:var(--red)}
.subscribe h2{position:absolute;left:100px;top:38px;font-family:"Prata",serif;font-size:28px;color:var(--white);font-weight:400;text-transform:uppercase}
.sub-input{position:absolute;left:600px;top:39px;width:300px;height:36px;background:var(--white);font-size:11px;color:#666;padding:11px 8px}
.subscribe .btn{position:absolute;left:914px;top:39px;height:36px;border-color:var(--white)}

/* team */
.team-bg{left:0;top:3165px;width:1200px;height:407px;background:var(--light)}
.team-text{left:300px;top:3312px;width:600px;text-align:center;font-size:11.5px;line-height:20px;color:#333}
.team-name{left:0;top:3374px;width:1200px;text-align:center;font-family:"Prata",serif;font-size:15px}

/* contact */
.field{background:var(--light);font-size:11px;color:#666;padding:12px 14px}

/* footer */
.footer-col h4{font-family:"Prata",serif;color:var(--red);font-size:18px;font-weight:400;margin-bottom:10px}
.footer-col li{list-style:none;font-size:12px;color:#ddd;line-height:26px}
.footer-contact div{display:flex;gap:14px;font-size:12px;color:#ddd;line-height:18px;margin-bottom:22px}
.social{display:flex;gap:8px}
.social span{width:30px;height:30px;border-radius:50%;border:2px solid var(--white);background:var(--red)}
.copyright{left:0;top:4430px;width:1200px;height:38px;background:var(--red);color:var(--white);font-size:11px;text-align:center;line-height:38px}
</style>
</head>
<body>

<!-- top bar -->
<div class="abs topbar">
  <span style="left:62px"><svg width="14" height="14" viewBox="0 0 24 24"><path d="M6 2l4 4-2 3c1 3 4 6 7 7l3-2 4 4-3 3C10 21 3 14 3 5z" fill="none" stroke="#d33a3a" stroke-width="2"/></svg>(615) 555-0142</span>
  <span style="left:566px"><svg width="14" height="16" viewBox="0 0 24 26"><path d="M12 2a8 8 0 0 0-8 8c0 6 8 14 8 14s8-8 8-14a8 8 0 0 0-8-8z" fill="none" stroke="#d33a3a" stroke-width="2"/><circle cx="12" cy="10" r="3" fill="#d33a3a"/></svg>1450 Maple Ridge Drive Suite 210, Westbrook Square</span>
  <span style="left:928px"><svg width="18" height="13" viewBox="0 0 24 16"><rect x="1" y="1" width="22" height="14" fill="none" stroke="#d33a3a" stroke-width="2"/><path d="M1 1l11 8 11-8" fill="none" stroke="#d33a3a" stroke-width="2"/></svg>office@pollardlawfirm-example.com</span>
</div>

<!-- nav -->
<header class="abs nav">
  <div class="logo">Pollard Law Firm</div>
  <nav class="menu">
    <span class="active">Home</span><span>About Us</span><span>News</span><span>Prectice Area</span><span>Our Team</span><span>Contact Us</span>
  </nav>
  <div class="call">
    <div class="ic"><svg width="18" height="18" viewBox="0 0 24 24"><path d="M6 2l4 4-2 3c1 3 4 6 7 7l3-2 4 4-3 3C10 21 3 14 3 5z" fill="#fff"/></svg></div>
    <div class="num">(615) 555-0187</div>
  </div>
</header>

<!-- hero -->
<section class="abs hero">
  <svg width="1200" height="700" class="abs" style="left:0;top:0">
    <defs>
      <linearGradient id="heroGrad" x1="0" y1="0" x2="1" y2="0.4">
        <stop offset="0" stop-color="#1a1414"/>
        <stop offset=".35" stop-color="#5a1a1c"/>
        <stop offset=".6" stop-color="#3a4148"/>
        <stop offset=".85" stop-color="#7a2226"/>
        <stop offset="1" stop-color="#1a1414"/>
      </linearGradient>
    </defs>
    <rect width="1200" height="700" fill="url(#heroGrad)" role="img" aria-label="Photo of a wrecked red car with shattered windshield"/>
    <polygon points="0,600 1200,430 1200,700 0,700" fill="#fff"/>
    <polygon points="0,580 1200,400 1200,412 0,600" fill="#fff"/>
    <polygon points="480,520 1200,380 1200,388" fill="#fff"/>
    <polygon points="700,440 1200,340 1200,352" fill="#fff"/>
    <polygon points="0,640 1200,460 1200,470 0,660" fill="#111"/>
  </svg>
  <h1>Don’t Lose What’s<br>Legally&nbsp; Yours</h1>
  <div class="btn"><div class="arrow"><svg width="16" height="14" viewBox="0 0 16 14"><path d="M1 1l14 6-14 6 4-6z" fill="#fff"/></svg></div><div class="label">Learn More</div></div>
</section>

<!-- about -->
<div class="abs eyebrow" style="left:62px;top:843px">Welcome To</div>
<h2 class="abs heading" style="left:62px;top:864px">About Us</h2>
<div class="abs about-text">
  <p>WE ARE TRIAL LAWYERS AND WE ARE PROUD OF IT! There are many law firms in Tennessee who claim to be trial lawyers, but their attorneys have never seen a courtroom. We have tried hundreds of cases to verdict and we have helped thousands of people in the Tennessee courts. We fight against billion dollar insurance companies, billion dollar corporations, and the State of Tennessee..and we win!</p>
  <p>It is very hard not to take each case personally. Our clients include victims of personal injury who did not ask for the pain from a car wreck</p>
</div>
<div class="abs btn" style="left:60px;top:1130px"><div class="arrow"><svg width="16" height="14" viewBox="0 0 16 14"><path d="M1 1l14 6-14 6 4-6z" fill="#fff"/></svg></div><div class="label">Learn More</div></div>
<svg class="abs" style="left:485px;top:775px" width="635" height="400">
  <polygon points="165,0 630,0 630,365 270,360" fill="#c9ccd0" role="img" aria-label="Photo of lawyers meeting with a client at a table"/>
  <polygon points="300,365 630,355 630,362 300,372" fill="#222"/>
  <polygon points="6,395 60,215 268,215 268,395" fill="#c8c8c8"/>
  <polygon points="16,385 66,225 258,225 258,385" fill="#7f97a8" role="img" aria-label="Photo of people inspecting a damaged car after a collision"/>
</svg>

<!-- quote band -->
<svg class="abs" style="left:0;top:1222px" width="1200" height="395">
  <rect y="0" width="1200" height="395" fill="#fff"/>
  <polygon points="0,130 1200,36 1200,360 0,395" fill="#d33a3a"/>
  <polygon points="0,395 1200,315 1200,395" fill="#1a1a1a"/>
  <polygon points="0,395 1200,340 1200,395" fill="#1e1e1e" opacity=".6"/>
  <rect x="190" y="0" width="200" height="395" rx="6" fill="#2a2a2a" role="img" aria-label="Photo of a smiling attorney in a dark suit"/>
</svg>
<div class="abs quote">“Speak up for those who cannot speak for themselves, for the rights of all who are destitute. Speak up and judge fairly; defend the rights of the poor and needy.”</div>

<!-- practice -->
<div class="abs eyebrow center" style="left:0;top:1703px;width:1200px">We Works</div>
<h2 class="abs heading" style="left:0;top:1722px;width:1200px;text-align:center">Practice Area</h2>

<div class="abs practice-item" style="left:243px;top:1872px">Personal Injury<a>LEARN MORE</a></div>
<div class="abs" style="left:445px;top:1807px;width:6px;height:262px;background:#bbb"></div>
<div class="abs photo" style="left:451px;top:1807px;width:173px;height:250px" role="img" aria-label="Photo of a crashed car"></div>

<div class="abs practice-item" style="left:641px;top:1912px">slip and fall<br>accidents<a>LEARN MORE</a></div>
<div class="abs" style="left:785px;top:1883px;width:6px;height:250px;background:#bbb"></div>
<div class="abs" style="left:791px;top:1883px;width:173px;height:248px;background:linear-gradient(135deg,#6f7c84,#c8a06a)" role="img" aria-label="Photo of a dog biting a hand"></div>

<div class="abs" style="left:236px;top:2008px;width:7px;height:262px;background:var(--red)"></div>
<div class="abs" style="left:243px;top:2008px;width:177px;height:250px;background:linear-gradient(135deg,#4a5a6a,#a8b0b8)" role="img" aria-label="Photo of a blood pressure check on an arm"></div>

<div class="abs practice-item" style="left:440px;top:2134px">Motor vehicle<br>accidents<a>LEARN MORE</a></div>
<div class="abs" style="left:584px;top:2074px;width:7px;height:262px;background:#bbb"></div>
<div class="abs" style="left:591px;top:2074px;width:172px;height:248px;background:linear-gradient(135deg,#9a9ea4,#d4c06a)" role="img" aria-label="Photo of a man fallen beside a wet floor sign"></div>

<div class="abs practice-item" style="left:815px;top:2152px">Dog bites<a>LEARN MORE</a></div>

<!-- news -->
<svg class="abs" style="left:0;top:2340px" width="1200" height="320">
  <polygon points="0,0 1200,120 1200,320 0,320" fill="#1a1a1a"/>
  <polygon points="560,80 1200,15 1200,180" fill="#d33a3a"/>
  <polygon points="0,320 1200,320 1200,312 0,312" fill="#b82a2a"/>
</svg>
<div class="abs eyebrow center" style="left:0;top:2463px;width:1106px">News</div>
<h2 class="abs heading" style="left:0;top:2484px;width:1106px;text-align:center;color:#fff">Letest News</h2>
<div class="abs" style="left:142px;top:2558px;width:916px;height:494px;background:#fff"></div>
<div class="abs" style="left:277px;top:2740px;width:136px;height:140px;background:var(--red)"></div>
<div class="abs" style="left:298px;top:2618px;width:338px;height:240px;background:linear-gradient(135deg,#e8e4df,#8a6a52)" role="img" aria-label="Photo of a lawyer consulting with a client"></div>
<div class="abs" style="left:787px;top:2690px;width:136px;height:130px;background:#ddd"></div>
<div class="abs news-card">
  <h3>Trucking Company Offers 6<br>Figure Settlement</h3>
  <p>On a Thursday afternoon, our client was traveling to work when suddenly a semi-truck ran through a stop sign and.</p>
  <a>READ MORE</a>
</div>
<div class="abs" style="left:502px;top:2876px;font-size:10px;display:flex;gap:10px;align-items:center">
  <span style="color:var(--red)">1</span><span style="width:30px;height:1px;background:var(--red)"></span><span>2</span><span>3</span>
</div>

<!-- subscribe -->
<section class="abs subscribe">
  <h2>Subsribe News Letters</h2>
  <div class="sub-input">Enter Email Address....</div>
  <div class="btn"><div class="arrow"><svg width="16" height="14" viewBox="0 0 16 14"><path d="M1 1l14 6-14 6 4-6z" fill="#fff"/></svg></div><div class="label">Subcribe Now</div></div>
</section>

<!-- team -->
<div class="abs team-bg">
  <svg width="1200" height="407"><polygon points="0,290 1200,180 1200,192 0,310" fill="#fff"/><polygon points="700,110 1200,60 1200,66" fill="#fff"/></svg>
</div>
<div class="abs eyebrow center" style="left:0;top:3236px;width:1200px">Attorney</div>
<h2 class="abs heading" style="left:0;top:3256px;width:1200px;text-align:center">Our Team</h2>
<div class="abs team-text">Daniel was born and raised in Clarksville, Tennessee. His mother is a retired elementary school teacher of 35 years and his father is a college professor at Riverbend College. With that kind of background, Daniel always knew he would either become a teacher or a lawyer.</div>
<div class="abs team-name">Daniel R. Pollard</div>
<svg class="abs" style="left:440px;top:3410px" width="320" height="150">
  <circle cx="63" cy="75" r="56" fill="#fff"/><circle cx="63" cy="75" r="50" fill="#5b6472" role="img" aria-label="Portrait of an attorney"/>
  <circle cx="254" cy="75" r="56" fill="#fff"/><circle cx="254" cy="75" r="50" fill="#5a3a36" role="img" aria-label="Portrait of an attorney"/>
  <circle cx="160" cy="75" r="72" fill="#fff" stroke="#ddd"/><circle cx="160" cy="75" r="64" fill="#8a7a70" role="img" aria-label="Portrait of Daniel R. Pollard"/>
</svg>

<!-- contact -->
<svg class="abs" style="left:60px;top:3640px" width="460" height="335">
  <polygon points="0,0 365,0 458,334 0,334" fill="#d33a3a"/>
  <polygon points="0,0 360,0 448,322 0,322" fill="#7a8088" role="img" aria-label="Photo of a distressed woman sitting beside a crashed car"/>
</svg>
<div class="abs eyebrow" style="left:602px;top:3652px">Get In Touch</div>
<h2 class="abs heading" style="left:600px;top:3672px">Contact Us</h2>
<div class="abs field" style="left:600px;top:3730px;width:262px;height:36px">Name :</div>
<div class="abs field" style="left:877px;top:3730px;width:262px;height:36px">Last Name :</div>
<div class="abs field" style="left:600px;top:3782px;width:262px;height:36px">Email :</div>
<div class="abs field" style="left:877px;top:3782px;width:262px;height:36px">Phone No :</div>
<div class="abs field" style="left:600px;top:3832px;width:539px;height:88px">How Can We Help ?</div>
<div class="abs btn" style="left:600px;top:3938px"><div class="arrow"><svg width="16" height="14" viewBox="0 0 16 14"><path d="M1 1l14 6-14 6 4-6z" fill="#fff"/></svg></div><div class="label" style="padding:0 30px">Submit</div></div>

<!-- footer -->
<svg class="abs" style="left:0;top:4060px" width="1200" height="370">
  <polygon points="0,70 1200,0 1200,370 0,370" fill="#161616"/>
  <polygon points="0,60 1200,10 1200,20 0,80" fill="#2a2a2a"/>
</svg>
<div class="abs logo" style="top:4176px;left:60px">Pollard Law Firm</div>
<div class="abs footer-col" style="left:337px;top:4176px">
  <h4>Site Map</h4>
  <ul><li>- Home</li><li>- About Us</li><li>- Prectice Area</li><li>- Our Team</li><li>- News</li><li>- Contact Us</li></ul>
</div>
<div class="abs footer-col footer-contact" style="left:612px;top:4176px">
  <h4>Contact Us</h4>
  <div><svg width="16" height="18" viewBox="0 0 24 26"><path d="M12 2a8 8 0 0 0-8 8c0 6 8 14 8 14s8-8 8-14a8 8 0 0 0-8-8z" fill="none" stroke="#d33a3a" stroke-width="2"/><circle cx="12" cy="10" r="3" fill="#d33a3a"/></svg><span>1450 Maple Ridge Drive | Suite 210<br>| Franklin, TN 37000</span></div>
  <div><svg width="18" height="13" viewBox="0 0 24 16"><rect x="1" y="1" width="22" height="14" fill="#d33a3a"/><path d="M1 1l11 8 11-8" fill="none" stroke="#161616" stroke-width="2"/></svg><span>office@pollardlawfirm-example.com</span></div>
  <div><svg width="16" height="16" viewBox="0 0 24 24"><path d="M6 2l4 4-2 3c1 3 4 6 7 7l3-2 4 4-3 3C10 21 3 14 3 5z" fill="#d33a3a"/></svg><span>(615) 555-0187</span></div>
</div>
<div class="abs footer-col" style="left:888px;top:4176px">
  <h4>Follow Us</h4>
  <div class="social"><span></span><span></span><span></span><span></span></div>
</div>
<div class="abs copyright">©2021 Pollard Law Firm, PLLC.&nbsp; All Rights Reserved.</div>

</body>
</html>
```